BrawnCrate placard

I need a placard designed that will go in my monthly subscription boxes to describe the products inside. There must be space to write 3-5 sentences on each product.
the first area will be titled: For your flowing mane
2 for your macho glow
3 to keep you smelling macho
4 to keep you clanging and banging at the gym.
Placard will be 5inchs wide and 7inchs long

I have attached the logo and the website address must be used in the design brawncrates.com.

Target Market(s)

men between 20-50

Colors

Designer to choose colors to be used in the design.

Requirements
Must have
• My website address brawncrates.com
• 4 area to write 3-5 sentences
• 1 for your flowing mane
• 2to keep you smelling macho
• 3 to keep you clanging and banging at the gym
• 4 for your macho glow

```html
<!DOCTYPE html>
<html lang="en">
<head>
<meta charset="utf-8">
<title>BrawnCrate Placard</title>
<link rel="stylesheet" href="https://fonts.googleapis.com/css2?family=Source+Sans+3:wght@400;600;700&family=Oswald:wght@600&display=swap">
<style>
  :root {
    --red: #e8141f;
    --black: #111111;
    --paper: #ececec;
    --ink: #333333;
    --bg: #c9c9cb;
    --white: #ffffff;
  }
  * { margin: 0; padding: 0; box-sizing: border-box; }
  html, body { width: 1200px; height: 1200px; overflow: hidden; }
  body {
    background: var(--bg);
    font-family: "Source Sans 3", sans-serif;
    position: relative;
  }
  .placard {
    position: absolute;
    top: 176px;
    width: 549px;
    height: 778px;
    background: var(--paper);
    overflow: hidden;
  }
  .placard--front { left: 30px; }
  .placard--back { left: 618px; }
  .top-chevron { position: absolute; top: 0; left: 0; }

  /* Front */
  .front-brand {
    position: absolute;
    top: 440px; left: 0; width: 100%;
    text-align: center;
  }
  .brand-name {
    display: inline-flex; align-items: center; gap: 12px;
    font-weight: 700;
    color: var(--black);
    letter-spacing: 2px;
  }
  .brand-mark {
    display: inline-block;
    background: var(--red);
  }
  .front-brand .brand-name { font-size: 46px; }
  .front-brand .brand-mark { width: 30px; height: 30px; }
  .tagline {
    font-family: "Oswald", sans-serif;
    font-weight: 600;
    color: var(--black);
    text-transform: uppercase;
    letter-spacing: -0.3px;
  }
  .front-brand .tagline { font-size: 12.5px; margin-top: 6px; }
  .front-band {
    position: absolute;
    left: 0; bottom: 0; width: 100%; height: 92px;
    background: var(--red);
    color: var(--white);
    font-size: 29px;
    display: flex; align-items: center; justify-content: center;
  }

  /* Back */
  .back-brand {
    position: absolute;
    top: 118px; left: 0; width: 100%;
    text-align: center;
  }
  .back-brand .brand-name { font-size: 20px; gap: 6px; letter-spacing: 1px; }
  .back-brand .brand-mark { width: 12px; height: 12px; }
  .back-brand .tagline { font-size: 6.5px; margin-top: 1px; }
  .back-title {
    position: absolute;
    top: 176px; left: 0; width: 100%;
    text-align: center;
    font-size: 17.5px;
    font-weight: 700;
    color: var(--black);
  }
  .product {
    position: absolute;
    left: 40px; width: 464px;
  }
  .product-title {
    color: var(--red);
    font-size: 14px;
    font-weight: 600;
    display: flex; align-items: center; gap: 6px;
  }
  .product-title::before {
    content: "";
    width: 5px; height: 5px;
    background: var(--black);
    transform: rotate(45deg);
  }
  .product-text {
    margin: 7px 0 0 5px;
    font-size: 11.2px;
    line-height: 14.8px;
    color: var(--ink);
    text-align: justify;
  }
  .footer {
    position: absolute;
    left: 0; bottom: 0; width: 100%; height: 150px;
    background: var(--black);
    color: var(--white);
  }
  .footer-shapes { position: absolute; top: 0; left: 0; }
  .contact-label {
    position: absolute; left: 40px; top: 24px;
    font-size: 11.5px; font-weight: 600; letter-spacing: 0.3px;
    padding-bottom: 4px;
    width: 162px;
    border-bottom: 1px solid #8a8a8a;
  }
  .contact-call {
    position: absolute; left: 35px; top: 49px;
    font-size: 14.5px; font-weight: 600; line-height: 19px;
    text-align: center;
  }
  .contact-email {
    position: absolute; right: 41px; top: 56px;
    font-size: 11.5px; font-weight: 600;
  }
  .footer-url {
    position: absolute; left: 0; top: 104px; width: 348px;
    text-align: right;
    font-size: 13.5px;
    line-height: 20px;
  }
  .social {
    position: absolute; top: 99px; left: 399px;
    display: flex; gap: 5px;
  }
  .social span {
    width: 30px; height: 30px; border-radius: 50%;
    background: var(--white);
  }
</style>
</head>
<body>

  <section class="placard placard--front">
    <svg class="top-chevron" width="549" height="100" viewBox="0 0 549 100">
      <polygon points="102,0 451,0 276,98" fill="var(--red)"/>
    </svg>
    <div class="front-brand">
      <div class="brand-name"><span class="brand-mark"></span>BrawnCrate</div>
      <div class="tagline">Mens grooming and essentials for the everyday macho man</div>
    </div>
    <div class="front-band">www.brawncrates.com.</div>
  </section>

  <section class="placard placard--back">
    <svg class="top-chevron" width="549" height="100" viewBox="0 0 549 100">
      <polygon points="101,0 451,0 274,88" fill="var(--red)"/>
    </svg>
    <div class="back-brand">
      <div class="brand-name"><span class="brand-mark"></span>BrawnCrate</div>
      <div class="tagline">Mens grooming and essentials for the everyday macho man</div>
    </div>
    <h1 class="back-title">GROOMING ESSENTIAL FOR THE EVERYDAY</h1>

    <article class="product" style="top:214px">
      <h2 class="product-title">For your flowing mane</h2>
      <p class="product-text">simply dummy text of the printing and typesetting industry. Lorem Ipsum has been the industry's standard dummy text ever since the 1500s, when an unknown printer took a galley of type and scrambled it to make a type specimen book. It has survived not only five centuries, but also the leap into electronic typesetting, remaining essentially unchanged.</p>
    </article>
    <article class="product" style="top:319px">
      <h2 class="product-title">To keep you smelling macho</h2>
      <p class="product-text">simply dummy text of the printing and typesetting industry. Lorem Ipsum has been the industry's standard dummy text ever since the 1500s, when an unknown printer took a galley of type and scrambled it to make a type specimen book. It has survived not only five centuries, but also the leap into electronic typesetting, remaining essentially unchanged.</p>
    </article>
    <article class="product" style="top:422px">
      <h2 class="product-title">To keep you clanging and banging at the gym</h2>
      <p class="product-text">simply dummy text of the printing and typesetting industry. Lorem Ipsum has been the industry's standard dummy text ever since the 1500s, when an unknown printer took a galley of type and scrambled it to make a type specimen book. It has survived not only five centuries, but also the leap into electronic typesetting, remaining essentially unchanged.</p>
    </article>
    <article class="product" style="top:526px">
      <h2 class="product-title">For your macho glow</h2>
      <p class="product-text">simply dummy text of the printing and typesetting industry. Lorem Ipsum has been the industry's standard dummy text ever since the 1500s, when an unknown printer took a galley of type and scrambled it to make a type specimen book. It has survived not only five centuries, but also the leap into electronic typesetting, remaining essentially unchanged.</p>
    </article>

    <footer class="footer">
      <svg class="footer-shapes" width="549" height="150" viewBox="0 0 549 150">
        <polygon points="372,0 549,0 549,12 380,12" fill="var(--red)"/>
        <polygon points="0,104 364,104 356,124 0,124" fill="var(--red)"/>
      </svg>
      <div class="contact-label">CONTACT US</div>
      <div class="contact-call">Call BrawnCrate toll free:<br>1-800-555-0142</div>
      <div class="contact-email">info@brawncrates.com</div>
      <div class="footer-url">www.brawncrates.com.</div>
      <div class="social"><span></span><span></span><span></span></div>
    </footer>
  </section>

</body>
</html>
```